Outdoor sign for Brightwater Auto Restoration

I need a horizontal 4'x 8' outdoor roadside sign for my classic auto restoration business. I have uploaded colors and our logo. Needs the Brightwater name, a prominent Classic AUTO RESTORATION, phone number and website. We rebuild and restore vintage cars, trucks and 4x4s. I'd like something clean but possibly retro. Classic Auto Restoration is more important than the Brightwater name. It needs to be visible and readable from the street. NO CLIP ART

Target Market(s)

Customers who need their vintage care restored or upgraded. Men and women ages 25-75

Industry/Entity Type

Automotive

Colors
FFC000
F8CF3A
FAE287
FDF2CF
FEFAEE

Requirements
Must have
• Legible. Bright. Readable as a backlit 4' x 8' large horizontal sign (roughly 120cm X 240cm)
Nice to have
• Use of the Brightwater logo/type, Complete or Classic before prominent AUTO RESTORATION
Should not have
• Clip art of old cars or icons. And we don't want the Brightwater Logo from the website because it wont be legible from the road. I have included the Illustrator file for Brightwater text in the uploads

```html
<!DOCTYPE html>
<html lang="en">
<head>
<meta charset="utf-8">
<title>Brightwater Auto Restoration – Roadside Sign</title>
<link rel="stylesheet" href="https://fonts.googleapis.com/css2?family=Pinyon+Script&family=Saira+Condensed:ital,wght@1,800&family=Roboto+Condensed:wght@700&display=swap">
<style>
  :root {
    --sign-yellow: #f8ae1a;
    --sign-ink: #221f20;
    --sign-white: #ffffff;
  }
  html, body {
    margin: 0;
    padding: 0;
    width: 1200px;
    height: 600px;
    overflow: hidden;
    background: var(--sign-yellow);
  }
  .sign {
    display: block;
    width: 1200px;
    height: 600px;
  }
  .sign-field { fill: var(--sign-yellow); }
  .footer-band { fill: var(--sign-ink); }
  .rule { fill: var(--sign-ink); }
  .kicker {
    font-family: "Pinyon Script", cursive;
    font-size: 118px;
    fill: var(--sign-ink);
  }
  .headline {
    font-family: "Saira Condensed", sans-serif;
    font-style: italic;
    font-weight: 800;
    font-size: 158px;
    fill: var(--sign-ink);
  }
  .phone, .business-name, .website {
    font-family: "Roboto Condensed", sans-serif;
    font-weight: 700;
  }
  .phone { font-size: 70px; fill: var(--sign-white); }
  .business-name { font-size: 94px; fill: var(--sign-yellow); }
  .website { font-size: 38px; fill: var(--sign-white); }
</style>
</head>
<body>
<svg class="sign" viewBox="0 0 1200 600" xmlns="http://www.w3.org/2000/svg" role="img" aria-label="Brightwater Classic Auto Restoration sign">
  <rect class="sign-field" x="0" y="0" width="1200" height="600"/>

  <text class="kicker" x="600" y="138" text-anchor="middle">Classic</text>

  <rect class="rule" x="0" y="211" width="1200" height="6"/>
  <text class="headline" x="37" y="357" textLength="1125" lengthAdjust="spacingAndGlyphs">AUTO RESTORATION</text>
  <rect class="rule" x="0" y="384" width="1200" height="5"/>

  <rect class="footer-band" x="0" y="442" width="1200" height="158"/>
  <text class="phone" x="37" y="546" textLength="301" lengthAdjust="spacingAndGlyphs">555-214-7730</text>
  <text class="business-name" x="393" y="555" textLength="415" lengthAdjust="spacingAndGlyphs">BRIGHTWATER</text>
  <text class="website" x="862" y="535" textLength="301" lengthAdjust="spacingAndGlyphs">brightwaterautoworks.com</text>
</svg>
</body>
</html>
```